New design of old website

We need a new design of our domain name reseller website.

quilanorte.com

we would also like new design for Logo and all.

the site will be in English and portuguesse,

Industry/Entity Type

Domain

```html
<!DOCTYPE html>
<html lang="en">
<head>
<meta charset="utf-8">
<title>Quilanorte — Domain Reseller</title>
<link href="https://fonts.googleapis.com/css2?family=Noto+Serif:wght@400;700&family=Roboto:wght@300;400;700&display=swap" rel="stylesheet">
<style>
:root{
  --paper:#f6f4f0;
  --accent:#e4584a;
  --ink:#2f2b28;
  --muted:#8a8682;
  --nav:#3b3633;
  --hero-top:#7d8d99;
  --hero-bottom:#5d6c78;
  --hero-text:#f4ecd9;
  --line:#dedad4;
  --red-icon:#d9392b;
  --coral-icon:#ea5a4a;
  --gold-icon:#d4b060;
  --sage-icon:#a9c6a4;
  --brand:#1f4e6e;
}
*{margin:0;padding:0;box-sizing:border-box}
html,body{width:854px;height:1200px;overflow:hidden}
body{background:var(--paper);font-family:"Roboto",Arial,sans-serif;color:var(--muted);position:relative}
.topline{position:absolute;left:0;top:0;width:854px;height:2px;background:var(--accent)}
.brand{position:absolute;left:30px;top:34px;display:flex;align-items:center;gap:12px}
.brand-dot{width:56px;height:56px;border-radius:50%;background:var(--brand)}
.brand-name{font-family:"Noto Serif",Georgia,serif;font-weight:700;font-size:30px;color:var(--ink)}
.nav{position:absolute;top:47px;left:404px;display:flex;align-items:center;height:45px;font-family:"Noto Serif",Georgia,serif;font-size:13px;color:var(--nav)}
.nav a{color:inherit;text-decoration:none;margin-right:35px}
.nav a.active{background:var(--accent);color:#fff;border-radius:5px;padding:0 10px;height:45px;line-height:45px;margin-right:36px}
.nav .caret{font-size:9px;margin-left:10px}
.hero{position:absolute;left:0;top:140px;width:854px;height:318px;background:linear-gradient(180deg,var(--hero-top),var(--hero-bottom));text-align:center}
.hero h1{font-family:"Noto Serif",Georgia,serif;font-weight:400;font-size:46px;line-height:51px;color:var(--hero-text);margin-top:37px}
.hero .arrow{position:absolute;top:158px}
.btn-primary{position:absolute;left:375px;top:212px;width:105px;height:44px;line-height:44px;background:var(--accent);color:#fff;border-radius:5px;font-family:"Noto Serif",Georgia,serif;font-size:13px;box-shadow:0 2px 3px rgba(0,0,0,.2)}
.feature{position:absolute;top:424px;width:180px}
.feature .badge{position:absolute;left:60px;top:0;width:64px;height:64px;border-radius:50%;background:var(--paper);box-shadow:0 1px 3px rgba(0,0,0,.25);display:flex;align-items:center;justify-content:center}
.feature .badge span{width:54px;height:54px;border-radius:50%}
.feature h2{margin-top:91px;font-family:"Noto Serif",Georgia,serif;font-weight:400;font-size:28px;color:var(--ink);letter-spacing:-.5px}
.feature p{margin-top:16px;font-size:12px;font-weight:300;line-height:17.8px;color:#7d7975}
.btn-more{display:inline-block;height:31px;line-height:29px;padding:0 13px;border:1px solid #d8d4ce;border-radius:5px;background:#f0eeea;font-size:12px;color:#4a4541}
.feature .btn-more{position:absolute;top:300px;left:0}
.section-title{position:absolute;font-family:"Noto Serif",Georgia,serif;font-weight:400;font-size:28px;color:var(--ink);letter-spacing:-.5px}
.cap-list{position:absolute;left:29px;top:864px;width:186px;list-style:none;border-top:2px solid var(--line)}
.cap-list li{height:42.5px;line-height:40px;border-bottom:1px solid var(--line);font-size:12px;font-weight:700;color:#7d7975}
.cap-body{position:absolute;left:232px;top:864px;width:391px;border-top:2px solid var(--accent)}
.cap-body p{margin-top:28px;font-size:12px;font-weight:300;line-height:17.8px;color:#7d7975;width:376px}
.cap-body .btn-more{margin-top:30px}
.news-nav{position:absolute;top:816px;left:796px;font-size:14px;color:var(--ink);display:flex;gap:14px}
.news-item{position:absolute;left:640px;width:186px}
.news-item p{width:116px;font-size:12px;font-weight:300;line-height:17.8px;color:#7d7975}
.news-item time{display:block;margin-top:11px;font-size:10px;color:var(--ink)}
.news-item .thumb{position:absolute;left:136px;top:2px;width:50px;height:50px;border:1px solid #ddd}
.news-divider{position:absolute;left:640px;top:964px;width:186px;height:1px;background:var(--line)}
.footer{position:absolute;left:0;top:1136px;width:854px;height:64px;background:#fff;border-top:1px solid #e2dfda}
.social{position:absolute;top:25px;left:748px;display:flex;gap:9px}
.social span{width:20px;height:20px;background:var(--accent);border-radius:2px}
</style>
</head>
<body>
<div class="topline"></div>

<header>
  <div class="brand"><span class="brand-dot"></span><span class="brand-name">Quilanorte</span></div>
  <nav class="nav">
    <a class="active" href="#">Home</a>
    <a href="#">Reseller</a>
    <a href="#">Services<span class="caret">↓</span></a>
    <a href="#">Clients</a>
    <a href="#">Contacts</a>
  </nav>
</header>

<section class="hero">
  <h1>Our work is dedicated to the<br>prosperity<br>of our clients!</h1>
  <svg class="arrow" style="left:16px" width="14" height="24" viewBox="0 0 14 24"><path d="M12 2 2 12l10 10" fill="none" stroke="#e8e8e8" stroke-width="1.5"/></svg>
  <svg class="arrow" style="right:16px" width="14" height="24" viewBox="0 0 14 24"><path d="M2 2l10 10L2 22" fill="none" stroke="#e8e8e8" stroke-width="1.5"/></svg>
  <a class="btn-primary">Read More</a>
</section>

<section class="feature" style="left:29px">
  <div class="badge"><span style="background:var(--red-icon)"></span></div>
  <h2>Globalization</h2>
  <p>Lorem ipsum dolor sit amet, conse ctetuer adipiscing elit, sed diam nonummy nibh euismod tincidunt ut laoreet dolore magna aliquam erat volutpat. Ut wisi enim ad minim veniam, quis nostrud exerci tation ullamcorper suscipit.</p>
  <a class="btn-more">More</a>
</section>
<section class="feature" style="left:233px">
  <div class="badge"><span style="background:var(--coral-icon)"></span></div>
  <h2>Research</h2>
  <p>Lorem ipsum dolor sit amet, conse ctetuer adipiscing elit, sed diam nonummy nibh euismod tincidunt ut laoreet dolore magna aliquam erat volutpat. Ut wisi enim ad minim veniam, quis nostrud exerci tation ullamcorper suscipit.</p>
  <a class="btn-more">More</a>
</section>
<section class="feature" style="left:436px">
  <div class="badge"><span style="background:var(--gold-icon)"></span></div>
  <h2>Development</h2>
  <p>Lorem ipsum dolor sit amet, conse ctetuer adipiscing elit, sed diam nonummy nibh euismod tincidunt ut laoreet dolore magna aliquam erat volutpat. Ut wisi enim ad minim veniam, quis nostrud exerci tation ullamcorper suscipit.</p>
  <a class="btn-more">More</a>
</section>
<section class="feature" style="left:640px">
  <div class="badge"><span style="background:var(--sage-icon)"></span></div>
  <h2>24/7 Support</h2>
  <p>Lorem ipsum dolor sit amet, conse ctetuer adipiscing elit, sed diam nonummy nibh euismod tincidunt ut laoreet dolore magna aliquam erat volutpat. Ut wisi enim ad minim veniam, quis nostrud exerci tation ullamcorper suscipit.</p>
  <a class="btn-more">More</a>
</section>

<h2 class="section-title" style="left:29px;top:804px">Explore Our Capabilities</h2>
<ul class="cap-list">
  <li>Process Management</li>
  <li>Customer Relationship</li>
  <li>Management</li>
  <li>Information Ecosystem</li>
  <li>Development &amp; Integration</li>
</ul>
<div class="cap-body">
  <p>Lorem ipsum dolor sit amet, consectetuer adipiscing elit, sed diam nonum my nibh euismod tincidunt ut laoreet dolore magna aliquam erat volutpat. Ut wisi enim ad minim veniam, quis nostrud exerci tation ullamcorper suscipit. lobortis nisl ut aliquip ex ea commodo consequat. Duis autem vel eum iriure dolor in hendrerit in vulputate velit esse molestie consequat, vel illum dolore eu feugiat nulla facilisis at vero eros et accumsan et iust odio dignissim qui blandit praes.</p>
  <a class="btn-more">More</a>
</div>

<h2 class="section-title" style="left:640px;top:804px">Our News</h2>
<div class="news-nav"><span>‹</span><span>›</span></div>
<article class="news-item" style="top:855px">
  <p>Lorem ipsum dolor sit amet, consectetuer adi piscing elit, se...</p>
  <time>April 28,2013</time>
  <div class="thumb" role="img" aria-label="Magnifying glass over a globe" style="background:linear-gradient(135deg,#f2f2f2,#9aa3ab)"></div>
</article>
<div class="news-divider"></div>
<article class="news-item" style="top:992px">
  <p>Lorem ipsum dolor sit amet, consectetuer adi piscing elit, se...</p>
  <time>April 28,2013</time>
  <div class="thumb" role="img" aria-label="Hands holding a young green sprout" style="background:linear-gradient(135deg,#f5f1ea,#e0a58a)"></div>
</article>

<footer class="footer">
  <div class="social"><span></span><span></span><span></span></div>
</footer>
</body>
</html>
```